Project Lists Banner for HVAC ecommerce store

We want a banner that showcases our project list feature that will allow customers to create list of products that they can select and quickly order. this will be a middle of page banner. It will replace this banner - https://www.brightsnapclip.com/image/40872316
Font: Noto Sans
Size: 938x300 px
Color Options: #0059E, #00BBE3, #C6C8C7
Text:
Create lists of frequently purchased SKU's for fast ordering.
- Warehouse Inventory
- Complete Systems
- Large Projects
- And More...
"Sign In" is the call to action button. make button with non rounded (square) boarders.
We don't want a computer screen in banner nor a person. You can look at our competitors below for ideas.
Our staging server is lintvale7.com for reference
Our competitors:
https://www.hollowmarksupply.com/
https://www.tolvexo.com/
https://www.quibo.com/
https://www.vesko.com/index.html
Target Market(s)
HVAC, B2B
Industry/Entity Type
HVAC
Look and feel

```html
<!DOCTYPE html>
<html lang="en">
<head>
<meta charset="utf-8">
<title>Project Lists Banner</title>
<link href="https://fonts.googleapis.com/css2?family=Noto+Sans:wght@400;700&display=swap" rel="stylesheet">
<style>
  :root {
    --page-bg: #fdfdfd;
    --banner-grey: #c6c8c7;
    --band-grey: #b3b5b4;
    --accent-blue: #00bbe3;
    --text-dark: #2b2b2b;
    --text-light: #ffffff;
  }
  * { margin: 0; padding: 0; box-sizing: border-box; }
  html, body {
    width: 1200px;
    height: 626px;
    overflow: hidden;
    background: var(--page-bg);
    font-family: "Noto Sans", sans-serif;
  }
  .banner {
    position: absolute;
    left: 131px;
    top: 163px;
    width: 938px;
    height: 300px;
    background: var(--banner-grey);
    overflow: hidden;
  }
  .banner-decor {
    position: absolute;
    inset: 0;
  }
  .headline {
    position: absolute;
    left: 288px;
    top: 40px;
    font-size: 29px;
    font-weight: 400;
    line-height: 40px;
    color: var(--text-dark);
  }
  .feature {
    position: absolute;
    font-size: 25px;
    font-weight: 700;
    line-height: 30px;
    color: var(--text-dark);
    white-space: nowrap;
  }
  .feature::before {
    content: "";
    position: absolute;
    left: 2px;
    top: -6px;
    width: 56px;
    height: 3px;
    background: var(--accent-blue);
  }
  .feature--warehouse { left: 289px; top: 144px; }
  .feature--systems   { left: 288px; top: 188px; }
  .feature--projects  { left: 612px; top: 143px; }
  .feature--more      { left: 614px; top: 192px; }
  .feature--warehouse::before,
  .feature--projects::before { display: block; }
  .feature--more::before { top: -8px; }
  .sign-in {
    position: absolute;
    left: 293px;
    top: 248px;
    width: 94px;
    height: 24px;
    background: var(--accent-blue);
    color: var(--text-light);
    font-size: 13px;
    line-height: 24px;
    text-align: center;
    text-decoration: none;
    letter-spacing: 0.3px;
    border-radius: 0;
  }
</style>
</head>
<body>
  <section class="banner">
    <svg class="banner-decor" width="938" height="300" viewBox="0 0 938 300" role="img" aria-label="Abstract textured frame and diagonal band shapes">
      <g fill="none" stroke="var(--band-grey)" stroke-width="28" opacity="0.8">
        <rect x="230" y="-90" width="180" height="180" transform="rotate(35 320 0)"/>
        <rect x="520" y="120" width="260" height="260" transform="rotate(-35 650 250)"/>
        <rect x="860" y="200" width="180" height="180" transform="rotate(-35 950 290)"/>
        <rect x="-40" y="200" width="150" height="150" transform="rotate(-35 35 275)"/>
      </g>
      <g fill="var(--band-grey)" opacity="0.7">
        <rect x="660" y="-40" width="34" height="420" transform="rotate(55 677 170)"/>
        <rect x="760" y="-80" width="30" height="320" transform="rotate(-35 775 80)"/>
      </g>
      <rect x="60" y="40" width="200" height="200" fill="none" stroke="var(--accent-blue)" stroke-width="30" opacity="0.85" transform="rotate(35 160 140)"/>
    </svg>

    <h1 class="headline">Create lists of frequently purchased<br>SKU's for fast ordering.</h1>

    <p class="feature feature--warehouse">Warehouse Inventory</p>
    <p class="feature feature--systems">Complete Systems</p>
    <p class="feature feature--projects">Large Projects</p>
    <p class="feature feature--more">And More...</p>

    <a class="sign-in" href="#">SIGN IN</a>
  </section>
</body>
</html>
```